4' x 8' Construction Project Sign, think of a very large business card

We need project signs for our construction sites, the sign will be mounted along the road so cars driving by can quickly read. the sign should be able to be read as cars drive by doing highway speed.

Think like your making a large business card

I would like to include "NOW HIRING" Superintendents, Project Managers, Pipe Foremen, Pipe Layers, and Equipment Operators

Description of services we provide should include

Civil Construction Services
Land Clearing
Excavation
Underground Utilities
Environmental Maintenance

The 2 objectives is to market to future clients and to recruit new employees

The sign will be mounted on posts at the entrance of our construction projects
Updates

Low design quality

Target Market(s)

Construction and land developers

Industry/Entity Type

Construction Company

Other font styles liked:
• Hypatia Sans Pro lite

Colors

Designer to choose colors to be used in the design.

Requirements
Must have
• Clean and easy to read
• Civil Construction Services
• Land Clearing
• Excavation
• Underground Utilities
• Road Construction

```html
<!DOCTYPE html>
<html lang="en">
<head>
<meta charset="utf-8">
<title>Harlow Brothers – Project Sign</title>
<link href="https://fonts.googleapis.com/css2?family=Alegreya+Sans:wght@500;700&display=swap" rel="stylesheet">
<style>
  :root {
    --page-bg: #e4e4e4;
    --navy: #1f3c88;
    --navy-deep: #172a5a;
    --ink-grey: #58585b;
    --panel-top: #d2d2d2;
    --panel-bottom: #ffffff;
    --photo-top: #1d3366;
    --photo-bottom: #05070d;
  }
  * { margin: 0; padding: 0; box-sizing: border-box; }
  html, body { width: 1200px; height: 1200px; overflow: hidden; }
  body {
    background: var(--page-bg);
    font-family: "Alegreya Sans", sans-serif;
    position: relative;
  }
  .sign {
    position: absolute;
    left: 50px; top: 325px;
    width: 1100px; height: 550px;
    background: linear-gradient(to bottom, var(--panel-top) 0%, #f2f2f2 45%, var(--panel-bottom) 65%);
    overflow: hidden;
  }
  .sign-shapes { position: absolute; inset: 0; }
  .brand-square {
    position: absolute; left: 340px; top: 60px;
    width: 105px; height: 105px;
    background: var(--navy);
  }
  .brand-divider {
    position: absolute; left: 486px; top: 33px;
    width: 2px; height: 163px;
    background: var(--ink-grey);
  }
  .brand-name {
    position: absolute; left: 506px; top: 56px;
    width: 570px;
    font-size: 63px; font-weight: 500;
    color: var(--navy);
    letter-spacing: 1px;
    line-height: 1;
    white-space: nowrap;
  }
  .brand-tagline {
    position: absolute; left: 508px; top: 124px;
    width: 570px;
    font-size: 36px; font-weight: 700;
    color: var(--ink-grey);
    letter-spacing: 15.5px;
    line-height: 1;
    white-space: nowrap;
  }
  .pill-label {
    position: absolute;
    color: #fff;
    text-align: center;
    line-height: 1;
    white-space: nowrap;
  }
  .pill-label--hiring { left: 519px; top: 236px; width: 303px; font-size: 42px; font-weight: 700; }
  .pill-label--services { left: 527px; top: 394px; width: 282px; font-size: 29px; font-weight: 500; }
  .list-line {
    position: absolute;
    left: 230px; width: 870px;
    text-align: center;
    color: var(--navy);
    font-size: 27px; font-weight: 500;
    line-height: 1;
    white-space: nowrap;
  }
  .list-line .item { margin: 0 7px; }
  .list-line .item::before {
    content: "";
    display: inline-block;
    width: 11px; height: 11px;
    background: var(--navy);
    margin-right: 9px;
    vertical-align: 4px;
  }
  .hiring-1 { top: 292px; left: 225px; }
  .hiring-2 { top: 323px; left: 230px; }
  .services-1 { top: 442px; left: 192px; }
  .services-2 { top: 473px; left: 192px; }
</style>
</head>
<body>
  <div class="sign">
    <svg class="sign-shapes" width="1100" height="550" viewBox="0 0 1100 550">
      <defs>
        <linearGradient id="photo-tone" x1="0" y1="0" x2="0" y2="1">
          <stop offset="0" stop-color="var(--photo-top)"/>
          <stop offset="0.55" stop-color="#0f1c3c"/>
          <stop offset="1" stop-color="var(--photo-bottom)"/>
        </linearGradient>
      </defs>
      <polygon role="img" aria-label="Photo of construction workers in silhouette at a site with rebar and a hanging concrete bucket against a dusk sky"
        points="0,0 309,0 215,550 0,550" fill="url(#photo-tone)"/>
      <polygon points="1100,253 1100,550 1024,550" fill="var(--navy-deep)"/>
      <path d="M523,232 L818,232 L792,275 L547,275 Z" fill="var(--navy)" stroke="#fff" stroke-width="12" stroke-linejoin="round"/>
      <path d="M523,232 L818,232 L792,275 L547,275 Z" fill="var(--navy)" stroke="var(--navy)" stroke-width="8" stroke-linejoin="round"/>
      <path d="M531,387 L805,387 L782,430 L554,430 Z" fill="var(--navy)" stroke="var(--navy)" stroke-width="8" stroke-linejoin="round"/>
    </svg>

    <div class="brand-square"></div>
    <div class="brand-divider"></div>
    <div class="brand-name">HARLOW BROTHERS</div>
    <div class="brand-tagline">CIVIL CONSTRUCTION</div>

    <div class="pill-label pill-label--hiring">NOW HIRING</div>
    <p class="list-line hiring-1"><span class="item">SUPERINTENDENTS</span><span class="item">PROJECT MANAGERS</span><span class="item">PIPE FOREMEN</span></p>
    <p class="list-line hiring-2"><span class="item">PIPE LAYERS</span><span class="item">EQUIPMENT OPERATORS</span></p>

    <div class="pill-label pill-label--services">Services We Provide</div>
    <p class="list-line services-1"><span class="item">CIVIL CONSTRUCTION SERVICES</span><span class="item">LAND CLEARING</span><span class="item">EXCAVATION</span></p>
    <p class="list-line services-2"><span class="item">UNDERGROUND UTILITIES</span><span class="item">ENVIRONMENTAL MAINTENANCE</span></p>
  </div>
</body>
</html>
```